Rollvane Supply .com

This website is simple!!!
Landing page background image should capture the customers attention!!! We will provide a image as a example of what we like. The purpose for this website is to provide customers with a clean easy way to request a quote for industrial casters and wheels by OEM’s as well as maintenance departments worldwide. Please see if you can follow our thought process below.
Customer comes to website, they are invited to Request a Quote by providing us with Manufacturer Name, Manufacturers Part # and quantity needed.
If this is not known the customer will complete will WP conversation format form answering about 10 questions
Or
Look up the part number in one of the 8 to 12 catalogs located in the Pagewhirl Deck format on our catalog page, or equal plug in .
When the client request a quote a account page will pop up request The following:
Clients first and last name
Email address
And optional questions
Company name and best contact number.
Once this is complete customer will hit SUBMIT.
The customers request will be in system. A email will be sent to Customer service notifying us the Quote Request has been made.
We will then build a quote for the customer with a good, better and best options. Customers Request a Quote submission may have more than one caster or wheel requested at a time, so website must allow this.
When the customer comes back into website there email address will come up as the account name and request a password be made for them. This will allow them to store quotes in their account for future needs. If quote is older than 30 day the system will trigger a button at the bottom of the quote for resubmit Request for updated quote.
Once customer reviews quote the quote can be Converted to order within the website.
Once Converted the system will send us a email and order will be processed.
We will need a Chat program that will text to CS the questions.
You will need to have high quality graphic design skills on your team.
We have found 2 plugins that would work nicely with our new website Pagewhirl decks to showcase our catalogs for customers to research and QuillKit conversation forms to complete request for quote form.
Just Ideas:
Very very ghosted caster blueprint in white background but very very ghosted or the icon just idea
We have never had a font used we like
Grayscale every except for rubber on wheels and logo icon
Website should have hamburger menu on left
Website should hav responsive deign
Account head on right side
Has anyone read the brief from top to bottom and the updates, I’m seeing a lot of duplicates of the website I posted in images I want a clean website With lite backgrand with the poly being definite colors on each wheel I added a green yellow and red image has anyone looked at that Just a question?
Went on vacation/holiday

```html
<!DOCTYPE html>
<html lang="en">
<head>
<meta charset="utf-8">
<title>Rollvane Supply – Home and Request A Quote</title>
<link href="https://fonts.googleapis.com/css2?family=Playfair+Display:wght@400;700&family=Mulish:wght@400;600;700&family=Poppins:wght@600&display=swap" rel="stylesheet">
<style>
:root{
  --brand:#2a4aa0;
  --brand-dark:#243f92;
  --brand-bright:#2f5ed6;
  --navy:#0d2a6e;
  --ink:#111;
  --hero-top:#f3f5f8;
  --hero-floor:#fbfbfb;
  --overlay:rgba(16,24,50,.92);
  --field-line:#9a9a9a;
  --page:#fff;
}
*{box-sizing:border-box;margin:0;padding:0}
html,body{width:1200px;height:1163px;overflow:hidden;background:var(--page)}
body{position:relative;font-family:'Mulish',sans-serif;color:var(--ink)}

.section-title{position:absolute;left:60px;font-family:'Poppins',sans-serif;font-weight:600;font-size:25px;color:var(--brand)}
.section-title.home{top:34px}
.section-title.quote{top:580px;left:58px}

.screen{position:absolute;left:60px;width:1080px;height:450px;overflow:hidden;background:var(--hero-floor);box-shadow:0 4px 10px rgba(0,0,0,.08)}
.screen.home{top:80px}
.screen.quote{top:623px}

.top-rule{position:absolute;left:0;top:0;width:100%;height:3px;background:var(--brand)}
.phone-band{position:absolute;right:0;top:0;width:300px;height:29px}
.phone{position:absolute;right:116px;top:4px;display:flex;align-items:center;gap:5px;color:#fff;font-size:9.5px;letter-spacing:.2px}
.phone-icon{width:21px;height:21px;border-radius:50%;background:#fff;display:flex;align-items:center;justify-content:center}

.brand{position:absolute;left:117px;top:22px;display:flex;align-items:center;gap:7px}
.brand-dot{width:14px;height:14px;border-radius:50%;background:var(--brand)}
.brand-name{font-weight:700;font-size:11px;color:var(--brand);letter-spacing:.1px}

.menu{position:absolute;left:905px;top:38px;display:flex;align-items:center;gap:7px;font-weight:700;font-size:9px;letter-spacing:.8px}
.menu-bars{width:22px;height:11px;display:flex;flex-direction:column;justify-content:space-between}
.menu-bars span{height:2px;background:var(--ink)}

.hero-band{position:absolute;left:0;top:57px;width:100%;height:201px;background:var(--hero-top)}
.hero-visual{position:absolute;left:430px;top:57px;width:650px;height:393px;
  clip-path:polygon(0 100%,24% 0,100% 0,100% 100%);
  background:
   linear-gradient(160deg,rgba(255,255,255,0) 40%,rgba(255,255,255,.6) 100%),
   linear-gradient(100deg,#c6c766 0%,#b9c06a 22%,#6a9dbf 38%,#3f78d8 55%,#62a2ff 75%,#e6eef8 100%)}

.hero-copy{position:absolute;left:117px;top:123px}
.kicker{font-family:'Playfair Display',serif;font-size:23px;line-height:1}
.headline{font-family:'Playfair Display',serif;font-weight:700;font-size:39px;line-height:1.1;margin-top:4px;letter-spacing:-.3px}
.easy{position:absolute;left:115px;top:220px;display:flex;align-items:center;gap:9px;font-size:12px}
.steps{display:flex;gap:2px}
.steps span{width:21px;height:21px;display:flex;align-items:center;justify-content:center;color:#fff;font-size:9px}
.steps span:nth-child(1){background:var(--brand-dark)}
.steps span:nth-child(2){background:#3457b8}
.steps span:nth-child(3){background:#4a70d3}
.process{position:absolute;left:116px;top:265px;list-style:none;font-size:10px;font-weight:600}
.process li{height:25px}
.process li::before{content:"•";color:var(--brand-bright);margin-right:3px}
.actions{position:absolute;left:116px;top:349px;display:flex;gap:9px}
.btn{height:30px;border-radius:15px;display:flex;align-items:center;justify-content:center;color:#fff;font-size:9.5px}
.btn.primary{width:127px;background:var(--brand-dark)}
.btn.secondary{width:97px;background:var(--brand-bright)}

.footer-bar{position:absolute;left:0;bottom:0;width:430px;height:23px;background:var(--brand);clip-path:polygon(0 0,100% 0,95% 100%,0 100%);color:#fff;font-size:8px;padding:6px 0 0 117px}

.shade{position:absolute;inset:0;background:var(--overlay)}
.modal{position:absolute;left:242px;top:63px;width:595px;height:324px;background:#fff;border-radius:15px}
.modal-title{position:absolute;left:70px;top:22px;font-family:'Playfair Display',serif;font-size:25px;font-weight:400}
.title-rule{position:absolute;left:70px;top:57px;width:305px;height:1px;background:#ddd}
.title-rule::before{content:"";position:absolute;left:0;top:-1px;width:86px;height:2px;background:var(--ink)}
.close{position:absolute;left:553px;top:13px;width:30px;height:30px;border-radius:50%;background:#ececec;display:flex;align-items:center;justify-content:center;font-size:11px}
.fields{position:absolute;left:70px;top:80px;width:456px;display:grid;grid-template-columns:224px 224px;column-gap:7px;row-gap:7px}
.field label{display:block;font-size:9.5px;height:12px;margin-bottom:4px}
.field .input{height:32px;border:1px solid var(--field-line)}
.submit{position:absolute;left:71px;top:248px;width:454px;height:33px;background:var(--navy);color:#fff;font-size:10px;display:flex;align-items:center;justify-content:center;letter-spacing:.3px}
</style>
</head>
<body>

<h2 class="section-title home">Home</h2>

<section class="screen home">
  <div class="top-rule"></div>
  <svg class="phone-band" viewBox="0 0 300 29" preserveAspectRatio="none"><path d="M0 0H300V29H40C25 29 18 0 0 0Z" fill="#2a4aa0"/></svg>
  <div class="phone"><span class="phone-icon"><svg width="10" height="10" viewBox="0 0 24 24"><path d="M6.6 10.8a15 15 0 0 0 6.6 6.6l2.2-2.2a1 1 0 0 1 1-.25 11 11 0 0 0 3.6.6 1 1 0 0 1 1 1V20a1 1 0 0 1-1 1A17 17 0 0 1 3 4a1 1 0 0 1 1-1h3.5a1 1 0 0 1 1 1 11 11 0 0 0 .6 3.6 1 1 0 0 1-.25 1Z" fill="#111"/></svg></span>+2 (555) 240 7310</div>
  <div class="brand"><span class="brand-dot"></span><span class="brand-name">ROLLVANE SUPPLY.COM</span></div>
  <div class="menu">MENU <span class="menu-bars"><span></span><span></span><span></span></span></div>

  <div class="hero-band"></div>
  <div class="hero-visual" role="img" aria-label="Swivel casters with coloured wheels standing on coloured stripes fanning across a white floor"></div>

  <div class="hero-copy">
    <p class="kicker">Solution For</p>
    <h1 class="headline">All Your Applications</h1>
  </div>
  <div class="easy">Easy As <span class="steps"><span>1</span><span>2</span><span>3</span></span></div>
  <ul class="process"><li>Request a Quote</li><li>Recive a Quote</li><li>Convert a Quote toOrder</li></ul>
  <div class="actions"><span class="btn primary">Request a Quote</span><span class="btn secondary">Catalog</span></div>
  <div class="footer-bar">Copyright © 2022 Rollvane Supply. All Rights Reserved.</div>
</section>

<h2 class="section-title quote">Request A Quote</h2>

<section class="screen quote">
  <div aria-hidden="true">
    <div class="top-rule"></div>
    <svg class="phone-band" viewBox="0 0 300 29" preserveAspectRatio="none"><path d="M0 0H300V29H40C25 29 18 0 0 0Z" fill="#2a4aa0"/></svg>
    <div class="phone"><span class="phone-icon"><svg width="10" height="10" viewBox="0 0 24 24"><path d="M6.6 10.8a15 15 0 0 0 6.6 6.6l2.2-2.2a1 1 0 0 1 1-.25 11 11 0 0 0 3.6.6 1 1 0 0 1 1 1V20a1 1 0 0 1-1 1A17 17 0 0 1 3 4a1 1 0 0 1 1-1h3.5a1 1 0 0 1 1 1 11 11 0 0 0 .6 3.6 1 1 0 0 1-.25 1Z" fill="#111"/></svg></span>+2 (555) 240 7310</div>
    <div class="brand"><span class="brand-dot"></span><span class="brand-name">ROLLVANE SUPPLY.COM</span></div>
    <div class="menu">MENU <span class="menu-bars"><span></span><span></span><span></span></span></div>
    <div class="hero-band"></div>
    <div class="hero-visual"></div>
    <div class="hero-copy"><p class="kicker">Solution For</p><p class="headline">All Your Applications</p></div>
    <div class="easy">Easy As <span class="steps"><span>1</span><span>2</span><span>3</span></span></div>
    <ul class="process"><li>Request a Quote</li><li>Recive a Quote</li><li>Convert a Quote toOrder</li></ul>
    <div class="actions"><span class="btn primary">Request a Quote</span><span class="btn secondary">Catalog</span></div>
    <div class="footer-bar">Copyright © 2022 Rollvane Supply. All Rights Reserved.</div>
  </div>
  <div class="shade"></div>

  <div class="modal" role="dialog" aria-label="Request A Quote">
    <h3 class="modal-title">Request A Quote</h3>
    <div class="title-rule"></div>
    <span class="close">X</span>
    <div class="fields">
      <div class="field"><label>First Name:</label><div class="input"></div></div>
      <div class="field"><label>Last Name:</label><div class="input"></div></div>
      <div class="field"><label>Email:</label><div class="input"></div></div>
      <div class="field"><label>Optional Question</label><div class="input"></div></div>
      <div class="field"><label>Company Name:</label><div class="input"></div></div>
      <div class="field"><label>Best Contact Number:</label><div class="input"></div></div>
    </div>
    <div class="submit">SUBMIT</div>
  </div>
</section>

</body>
</html>
```